TBrenwick Business Cards & Letterhead

I have a logo but need a design for some new business cards. We are a Design-Build Firm that specializes in the design and construction of commercial projects.
the cards need to be professional. no cartoon stuff.
i would like to have the cards in AI format so I can update the card as needed. Logo is provided.
Our Address is: 4718 Fenmoor Ct. Dalewood, West Virginia 26501

```html
<!DOCTYPE html>
<html lang="en">
<head>
<meta charset="utf-8">
<title>TBrenwick Business Card</title>
<link rel="stylesheet" href="https://fonts.googleapis.com/css2?family=Roboto:wght@400;700;900&display=swap">
<style>
  :root {
    --stage: #999999;
    --card-dark-a: #444444;
    --card-dark-b: #585858;
    --card-light: #ffffff;
    --ink: #444444;
    --ink-soft: #555555;
    --accent: #1a6fb0;
    --accent-deep: #1d5f94;
    --brand-text: #ffffff;
  }
  html, body {
    margin: 0;
    padding: 0;
    width: 1200px;
    height: 1000px;
    overflow: hidden;
    background: var(--stage);
    font-family: "Roboto", Arial, sans-serif;
  }
  .stage {
    position: relative;
    width: 1200px;
    height: 1000px;
  }
  .card {
    position: absolute;
    left: 293px;
    width: 615px;
    height: 351px;
    overflow: hidden;
  }
  .card-front {
    top: 110px;
    border-radius: 30px 30px 150px 30px / 30px 30px 160px 30px;
    background: linear-gradient(135deg, var(--card-dark-a), var(--card-dark-b));
  }
  .front-texture {
    position: absolute;
    inset: 0;
  }
  .brand {
    position: absolute;
    left: 54px;
    top: 263px;
    display: flex;
    align-items: center;
    gap: 8px;
  }
  .brand-square {
    width: 41px;
    height: 41px;
    background: var(--accent);
  }
  .brand-name {
    font-weight: 900;
    font-size: 50px;
    line-height: 1;
    letter-spacing: 0.5px;
    color: var(--brand-text);
  }
  .card-back {
    top: 519px;
    border-radius: 30px 30px 30px 170px / 30px 30px 30px 170px;
    background: var(--card-light);
  }
  .contact {
    position: absolute;
    left: 58px;
    width: 200px;
    top: 87px;
    text-align: center;
    font-size: 15px;
    line-height: 19px;
    color: var(--ink-soft);
  }
  .contact p { margin: 0; }
  .person-name {
    font-weight: 700;
    font-size: 16px;
    color: var(--ink);
  }
  .person-role { color: var(--ink-soft); }
  .divider {
    width: 53px;
    height: 2px;
    background: var(--accent);
    margin: 6px auto 16px;
  }
  .address { margin-bottom: 19px !important; }
  .reach { margin-bottom: 20px !important; }
  .website {
    font-weight: 700;
    color: var(--accent-deep);
  }
</style>
</head>
<body>
<main class="stage">
  <section class="card card-front">
    <div class="front-texture" role="img" aria-label="Subtle embossed repeating brand pattern on dark grey"></div>
    <div class="brand">
      <span class="brand-square"></span>
      <span class="brand-name">TBRENWICK</span>
    </div>
  </section>

  <section class="card card-back">
    <div class="contact">
      <p class="person-name">TOBIAS BRENWICK</p>
      <p class="person-role">President</p>
      <div class="divider"></div>
      <p class="address">4718 Fenmoor Ct. Dalewood<br>West Virginia 26501</p>
      <p class="reach">304-555-0142<br>tobias@tbrenwick.com</p>
      <p class="website">tbrenwick.com</p>
    </div>
  </section>
</main>
</body>
</html>
```